Web design for a dental and eye clinic

We need a web design for a dental and eye clinic ( with medical laboratory services) with two branches in Lagos Nigeria. The ultimate aim is to attract more patronage. The design should have links to social media and should have provision for appointments and enquiries. Blue should be part of the colours

Name of facility. VORANTACARE Added Saturday, May 27, 2017

Target Market(s)

Lagos. Nigeria

Industry/Entity Type

Health Care

Number of Pages Required

3 page

Font styles to use
Sans Serif

Colors
85cae6
cadf82

Requirements
Must have
• a projection of the professioal services rendered
Nice to have
• portal for enquiries and appointments
• Link to our facebook, twitter and instagram

```html
<!DOCTYPE html>
<html lang="en">
<head>
<meta charset="utf-8">
<title>Vorantacare – Dental &amp; Eye</title>
<link rel="stylesheet" href="https://fonts.googleapis.com/css2?family=Lato:wght@300;400;700&family=Roboto:wght@400;500;700&display=swap">
<style>
:root{
  --blue:#00aeef;
  --navy:#2b2a7a;
  --orange:#fdb515;
  --ink:#3d3d3d;
  --muted:#6b6b6b;
  --footer:#262626;
  --white:#ffffff;
}
*{margin:0;padding:0;box-sizing:border-box}
html,body{width:921px;height:1200px;overflow:hidden;background:var(--white)}
body{position:relative;font-family:'Lato',sans-serif;color:var(--ink)}
.abs{position:absolute}

/* header */
.header{left:0;top:0;width:921px;height:74px;background:var(--blue)}
.brand-panel{left:0;top:0;width:282px;height:74px;background:var(--white);border-left:1px solid var(--navy);border-bottom:1px solid var(--navy)}
.brand{left:124px;top:24px;display:flex;align-items:center;gap:7px;font-family:'Lato',sans-serif;font-weight:700;font-size:19px;color:var(--blue)}
.brand-dot{width:14px;height:14px;border-radius:50%;background:var(--blue)}
.contact-item{top:5px;font-family:'Roboto',sans-serif;font-size:10.5px;line-height:13px;color:var(--white)}
.contact-item svg{position:absolute;left:0;top:1px}
.contact-item span{display:block;padding-left:14px}
.hours{left:503px;top:0;width:166px;height:36px;background:var(--orange);padding:5px 0 0 8px}
.nav{left:355px;top:46px;display:flex;font-family:'Roboto',sans-serif;font-size:10px;color:var(--white)}
.nav a{color:var(--white);text-decoration:none;padding:0 12px;position:relative}
.nav a.active::after{content:"";position:absolute;left:9px;right:9px;top:22px;height:4px;background:var(--navy)}

/* hero */
.hero-photo{left:0;top:74px;width:921px;height:405px;background:linear-gradient(90deg,#c99c84 0%,#e4c2ae 30%,#eee4dc 55%,#e8eef2 75%,#dfe7ec 100%)}
.hero-title{left:553px;top:222px;font-size:34px;font-weight:700;color:var(--ink);letter-spacing:-.5px}
.hero-title em{font-style:normal;color:var(--blue)}
.hero-text{left:553px;top:268px;width:232px;font-size:10px;line-height:14.5px;color:#333}
.btn-appoint{left:553px;top:327px;width:153px;height:32px;border-radius:4px;background:var(--orange);color:var(--white);font-size:10.5px;font-weight:700;display:flex;align-items:center;justify-content:center;letter-spacing:.2px}

/* intro */
.intro-title{left:0;width:921px;top:498px;text-align:center;font-size:30px;font-weight:400;color:var(--ink)}
.intro-text{left:170px;width:581px;top:543px;text-align:center;font-size:11px;line-height:15px;font-weight:300;color:var(--muted)}
.card{top:590px;height:133px;background:var(--blue);color:var(--white)}
.card svg{position:absolute;left:5px;top:14px}
.card h3{position:absolute;left:56px;top:13px;font-family:'Roboto',sans-serif;font-weight:700;font-size:13.5px;line-height:17px}
.card p{position:absolute;left:56px;font-size:9.5px;line-height:14.5px}
.card .more{position:absolute;left:56px;top:106px;font-family:'Roboto',sans-serif;font-weight:700;font-size:8.5px}

/* eye */
.eye-photo{left:0;top:770px;width:921px;height:316px;background:linear-gradient(120deg,#5a4a42 0%,#6f6058 35%,#5d6470 65%,#4e4540 100%)}
.eye-title{left:0;width:921px;top:856px;text-align:center;font-size:30px;font-weight:700;color:var(--white)}
.eye-title em{font-style:normal;font-weight:400;color:var(--blue)}
.eye-text{left:190px;width:541px;text-align:center;font-size:9.8px;line-height:15px;color:var(--white)}

/* footer */
.footer{left:0;top:1086px;width:921px;height:114px;background:var(--footer);color:var(--white)}
.f-head{font-size:11.5px;line-height:14px}
.social{top:1136px;width:26px;height:26px;background:var(--white);border-radius:3px}
.copy{left:124px;top:1172px;font-size:8.5px}
.signup{left:352px;top:1141px;display:flex;height:28px}
.signup .field{width:157px;background:var(--white);color:#888;font-size:9.5px;padding:8px 0 0 9px}
.signup .go{width:61px;background:var(--orange);font-family:'Roboto',sans-serif;font-size:10px;padding:9px 0 0 10px}
.f-right{left:613px;top:1106px;width:250px}
.f-right h4{font-weight:400;font-size:11.5px;line-height:14px;letter-spacing:.2px}
.f-right p{margin-top:7px;font-size:11.5px;line-height:15px}
</style>
</head>
<body>

<header class="abs header"></header>
<div class="abs brand-panel"></div>
<div class="abs brand"><span class="brand-dot"></span>Vorantacare</div>

<div class="abs contact-item" style="left:392px">
  <svg width="10" height="10" viewBox="0 0 24 24"><path fill="#fff" d="M6.6 10.8a15.1 15.1 0 0 0 6.6 6.6l2.2-2.2c.3-.3.7-.4 1-.2 1.1.4 2.3.6 3.6.6.6 0 1 .4 1 1V20c0 .6-.4 1-1 1C10.6 21 3 13.4 3 4c0-.6.4-1 1-1h3.5c.6 0 1 .4 1 1 0 1.3.2 2.5.6 3.6.1.3 0 .7-.2 1z"/></svg>
  <span>Call Us Today<br>(+015)-555-01234</span>
</div>
<div class="abs hours contact-item">
  <svg width="10" height="10" viewBox="0 0 24 24" style="left:8px;top:6px"><circle cx="12" cy="12" r="10" fill="none" stroke="#fff" stroke-width="3"/><path d="M12 6v6l4 2" stroke="#fff" stroke-width="3" fill="none"/></svg>
  <span>Opening Hour<br>&nbsp;&nbsp;&nbsp;Mon - Sat: 9.00 am - 5.00 pm</span>
</div>
<div class="abs contact-item" style="left:679px">
  <svg width="12" height="10" viewBox="0 0 24 18"><rect x="1.5" y="1.5" width="21" height="15" rx="2" fill="none" stroke="#fff" stroke-width="2.5"/><path d="M2 3l10 7 10-7" fill="none" stroke="#fff" stroke-width="2.5"/></svg>
  <span>Email Us Via<br>&nbsp;info@vorantacare.com</span>
</div>

<nav class="abs nav">
  <a class="active">HOME</a><a>ABOUT US</a><a>ADULT SERVICES</a><a>EYE SURGERY</a><a>LOCATIONS</a><a>CONTACT</a>
</nav>

<div class="abs hero-photo" role="img" aria-label="Photo of a smiling couple close together on a bright background"></div>
<h1 class="abs hero-title"><em>Splendid</em> Smiles!</h1>
<p class="abs hero-text">Nullam malesuada mauris dolor, vel fringilla lectus accumsan vel. Mauris volutpat pulvinar nisi, quis commodo eros consectetur non...</p>
<div class="abs btn-appoint">MAKE AN APPOINTMENT</div>

<h2 class="abs intro-title">Vorantacare Dentistry</h2>
<p class="abs intro-text">Curabitur molestie venenatis augue, non mattis magna hendrerit nec. Suspendisse semper, metus eget ultricies malesuada, nulla ante commodo dolor, id laoreet magna.</p>

<section class="abs card" style="left:122px;width:229px">
  <svg width="46" height="72" viewBox="0 0 46 72"><path d="M6 6c8-5 14-2 17 0 3-2 9-5 17 0 6 5 4 16 1 22H5C2 22 0 11 6 6z" fill="none" stroke="#fff" stroke-width="2.5"/><path d="M16 30h14l-2 36h-10z" fill="none" stroke="#fff" stroke-width="2.5"/><path d="M15 38h16M15 46h16M16 54h14" stroke="#fff" stroke-width="2"/></svg>
  <h3>Getting Braces<br>A Painless Process</h3>
  <p style="top:55px">At Dental getting braces is a simple, painless process. To good to be true you say? Let us show you how.</p>
  <span class="more">LEARN MORE</span>
</section>
<section class="abs card" style="left:354px;width:228px">
  <svg width="44" height="54" viewBox="0 0 44 54"><path d="M22 2l19 7v15c0 14-9 23-19 28C12 47 3 38 3 24V9z" fill="none" stroke="#fff" stroke-width="2.5"/><path d="M13 18c5-3 7-1 9 0 2-1 4-3 9 0 3 4 0 12-2 20-1 3-3 3-4 0l-3-7-3 7c-1 3-3 3-4 0-2-8-5-16-2-20z" fill="none" stroke="#fff" stroke-width="2.2"/></svg>
  <h3>We Make Braces<br>Affordable</h3>
  <p style="top:55px">With a variety of payment options, getting braces from Dental is pain-free for your mouth and your wallet.</p>
  <span class="more">LEARN MORE</span>
</section>
<section class="abs card" style="left:586px;width:212px">
  <svg width="40" height="60" viewBox="0 0 40 60"><path d="M7 16C7 6 14 2 21 2c8 0 13 5 13 12 0 11-12 11-12 22" fill="none" stroke="#fff" stroke-width="7"/><circle cx="22" cy="50" r="5" fill="#fff"/></svg>
  <h3>Treatment FAQs</h3>
  <p style="top:40px">Got questions? Chances are they've been asked before. Answers are just a click away!</p>
</section>

<div class="abs eye-photo" role="img" aria-label="Photo of a child having an eye examination at a slit-lamp instrument, darkened"></div>
<h2 class="abs eye-title"><em>Eye</em> Treatment</h2>
<p class="abs eye-text" style="top:906px">We love kids! Putting children on the path to oral health is key to giving them lifetime of health. Our pediatric dentistry experts are passionate about giving a beautiful smile to every child who hops and skips through our doors.</p>
<p class="abs eye-text" style="top:950px">The top misconception about braces is that they are unaffordable. At Dental, you'll see that nothing could be further from the truth. Let us show you how to get a beautiful and budget-friendly smile!</p>

<footer class="abs footer"></footer>
<div class="abs f-head" style="left:124px;top:1106px;color:#fff">Follow us on Social Media</div>
<div class="abs social" style="left:123px" aria-label="Social link one"></div>
<div class="abs social" style="left:162px" aria-label="Social link two"></div>
<div class="abs social" style="left:202px" aria-label="Social link three"></div>
<div class="abs copy" style="color:#fff">© 2017 Vorantacare -&nbsp; All Rights Reserved</div>

<div class="abs f-head" style="left:354px;top:1106px;color:#fff">Sign up and have exclusive offers<br>sent to your inbox:</div>
<div class="abs signup" style="color:#fff"><div class="field">Email..</div><div class="go">SIGN UP</div></div>

<div class="abs f-right" style="color:#fff">
  <h4>PERSPICIATIS UNDE OMNIS ISTE NATUS VOLUPTATEM.</h4>
  <p>Lorem ipsum dolor sit amet,<br>cmassa. Cum sociis natoque tibus</p>
</div>

</body>
</html>
```